Consulting, Investors, Joint Venture Website

Founded in April 2018, Marendo Consultants Limited (MCL) is an advisory consulting firm specializing in engaging investors in business ventures in Tanzania.
With extensive experience in construction, energy, oil and gas and the legal professions, our team assembles our expertise that allows foreign investors to set foot and flourish in the Tanzanian market.
MCL is locally owned, founded and registered. Our shareholders are cultured Tanzanian citizens with extensive corporate experience in South Africa, Tanzania, United Kingdom and the United States.

Our mission is to provide responsive and unrivalled professional advice from learned and experienced professionals versed in the local market, with an understanding of the cultural and logistical challenges faced by foreign investors.

Our vision is to provide a complete investor’s package that initiates with company registration, compliance and documentation services and ultimately operational facilitation services.

Target Market(s)

Foreign Investors, International companies

Industry/Entity Type

Business Consultant

Number of Pages Required

5+ page

Requirements
Must have
• It will be 5 pages - Home, About Us, Services, Portfolio, Contact Us
Nice to have
• if it can look like https://www.plorvex.example/
• or https://www.dunetri.example or http://www.quillbrook.example/

```html
<!DOCTYPE html>
<html lang="en">
<head>
<meta charset="utf-8">
<title>Marendo Consultants</title>
<link href="https://fonts.googleapis.com/css2?family=Roboto:wght@400;500;700;900&family=Open+Sans:wght@400;600;700&display=swap" rel="stylesheet">
<style>
:root{
  --blue:#0d4fa0;
  --orange:#f28c1b;
  --ink:#111;
  --text:#555;
  --grey-bg:#ebebeb;
  --topbar:#000;
  --footer:#232323;
  --footer-bottom:#141414;
  --footer-text:#aaa;
  --white:#fff;
}
*{margin:0;padding:0;box-sizing:border-box}
html,body{width:1200px;height:2885px;overflow:hidden}
body{position:relative;font-family:"Open Sans",Arial,sans-serif;font-size:11px;color:var(--text);background:var(--white)}
.abs{position:absolute}

/* top bar */
.topbar{left:0;top:0;width:1200px;height:33px;background:var(--topbar);color:#fff;font-size:11px}
.topbar .mail{left:162px;top:9px}
.topbar .call{left:923px;top:9px}
.topbar svg{vertical-align:-2px;margin-right:6px}

/* hero */
.hero{left:0;top:33px;width:1200px;height:702px;background:var(--grey-bg)}
.brand{left:162px;top:52px;height:40px;display:flex;align-items:center;gap:10px;font-family:"Roboto",sans-serif;font-weight:700;font-size:17px;color:var(--blue);letter-spacing:.5px;white-space:nowrap}
.brand .mark{width:40px;height:40px;background:var(--blue)}
.nav{left:481px;top:33px;height:69px;display:flex;align-items:center;font-family:"Roboto",sans-serif;font-size:12px;font-weight:500;color:#222}
.nav a{color:inherit;text-decoration:none;padding:0 19px;border-right:1px solid #999;line-height:14px}
.nav a:last-child{border:0}
.nav a.active{background:var(--blue);color:#fff;height:69px;line-height:69px;padding:0 12px;border:0;margin-right:12px}
.social{left:946px;top:72px;display:flex;gap:14px}
.social span{width:11px;height:11px;border-radius:50%;background:#666}
.hero-card{left:27px;top:246px;width:948px;height:419px;background:var(--white)}
.hero-photo{left:475px;top:123px;width:725px;height:487px;background:linear-gradient(135deg,#c9ced3,#8c949c 45%,#e2e4e6)}
.hero-title{left:162px;top:332px;font-family:"Roboto",sans-serif;font-weight:900;font-size:58px;line-height:60px;color:var(--ink);white-space:nowrap}
.hero-rule{left:162px;top:483px;width:73px;height:1px;background:#555}
.hero-text{left:244px;top:476px;width:200px;font-size:11px;line-height:18px;color:#555}
.btn{display:inline-block;background:var(--blue);color:#fff;font-family:"Roboto",sans-serif;font-weight:500;font-size:12px;text-decoration:none}
.hero-btn{left:162px;top:535px;width:111px;height:40px;line-height:40px;text-align:center}
.dots{left:490px;top:627px;display:flex;gap:6px}
.dots span{width:6px;height:6px;background:#bbb}
.dots span.on{background:#222}

/* section titles */
.sec-title{left:0;width:1200px;display:flex;justify-content:center;align-items:center;gap:10px;font-family:"Roboto",sans-serif;font-weight:500;font-size:24px;color:#1b2a4a}
.sec-title .mark{width:30px;height:30px;background:#222}
.sec-title .bar{width:1px;height:30px;background:#888}

/* services */
.service{width:200px;height:279px;background:var(--white);border:1px solid #d5d5d5;border-left:6px solid var(--blue)}
.service::before{content:"";position:absolute;left:-6px;top:-1px;width:96px;height:6px;background:var(--blue)}
.service .icon{position:absolute;left:20px;top:40px;width:44px;height:44px}
.service h3{position:absolute;left:20px;top:107px;font-family:"Roboto",sans-serif;font-size:12px;font-weight:700;color:#111;white-space:nowrap}
.service p{position:absolute;left:20px;top:130px;width:160px;font-size:10.5px;line-height:21px;color:#555}
.service .more{position:absolute;left:92px;top:200px;width:110px;height:42px;line-height:42px;text-align:center;background:var(--orange);color:#fff;font-size:11px;font-weight:600}

/* about */
.about{left:0;top:1279px;width:1200px;height:515px;background:radial-gradient(ellipse at 50% 50%,#59606a,#2b2f35 75%)}
.about-text{left:162px;top:1424px;width:876px;text-align:center;color:#fff;font-size:12px;line-height:25px;text-transform:uppercase}
.pillar{width:320px;text-align:center;color:#fff}
.pillar svg{display:block;margin:0 auto}
.pillar h4{font-family:"Roboto",sans-serif;font-size:17px;font-weight:500;margin:10px 0}
.pillar p{font-size:11px;line-height:21px;color:#e6e6e6}

/* portfolio */
.pf-text{left:269px;top:1923px;width:204px}
.pf-text h3{font-family:"Roboto",sans-serif;font-size:14px;font-weight:700;color:#111;margin-bottom:8px}
.pf-text p{font-size:10.5px;line-height:19px;color:#777}
.pf-btn{left:271px;top:2050px;width:110px;height:42px;line-height:42px;text-align:center}
.pf-rule{left:271px;top:2116px;width:200px;height:2px;background:#bbb}
.tile{background:linear-gradient(135deg,#b7c3cf,#dfe4ea)}
.tile.dark{background:linear-gradient(135deg,#4f5d6c,#7d8a98)}
.tile.warm{background:linear-gradient(135deg,#c9b8a6,#e6ded4)}

/* footer */
.footer{left:0;top:2525px;width:1200px;height:327px;background:var(--footer)}
.f-brand{left:162px;top:2587px;display:flex;align-items:center;gap:14px;font-family:"Roboto",sans-serif;font-weight:700;font-size:20px;color:var(--orange);white-space:nowrap}
.f-brand .line{width:80px;height:1px;background:#888}
.f-about{left:162px;top:2630px;width:300px;font-size:11px;line-height:23px;color:var(--footer-text)}
.f-social{left:162px;top:2766px;display:flex;gap:13px}
.f-social span{width:10px;height:10px;border-radius:50%;background:var(--orange)}
.f-head{font-family:"Roboto",sans-serif;font-weight:700;font-size:12px;color:#fff}
.f-contact{left:563px;top:2594px;width:230px;font-size:11px;line-height:23px;color:var(--footer-text)}
.f-contact .web{color:#fff;font-weight:600}
.f-links{left:831px;top:2594px;width:207px;font-size:11px;color:var(--footer-text)}
.f-links li{list-style:none;border-bottom:1px solid #3a3a3a;line-height:38px}
.copy{left:0;top:2852px;width:1200px;height:33px;background:var(--footer-bottom);color:#bbb;font-size:10.5px;text-align:center;line-height:33px}
</style>
</head>
<body>

<div class="abs topbar">
  <div class="abs mail"><svg width="12" height="10" viewBox="0 0 12 10"><path d="M1 4 6 0l5 4v6H1z" fill="none" stroke="#fff"/></svg>E-mail : info@marendoconsultants.example</div>
  <div class="abs call"><svg width="11" height="11" viewBox="0 0 11 11"><path d="M2 0l2 3-1 1a7 7 0 0 0 4 4l1-1 3 2-1 2C5 11 0 6 0 2z" fill="#fff"/></svg>Call : +1000555012</div>
</div>

<section class="abs hero"></section>
<div class="abs brand"><span class="mark"></span>MARENDO CONSULTANTS</div>
<nav class="abs nav">
  <a class="active" href="#">Home</a><a href="#">About Us</a><a href="#">Services</a><a href="#">Portfolio</a><a href="#">Contact Us</a>
</nav>
<div class="abs social"><span></span><span></span><span></span><span></span></div>
<div class="abs hero-card"></div>
<div class="abs hero-photo" role="img" aria-label="Photo of business people in a meeting around a conference table"></div>
<h1 class="abs hero-title">Welcome To Marendo<br>Consultants</h1>
<div class="abs hero-rule"></div>
<p class="abs hero-text">Lorem Ipsum is simply dummy text of the printing industry.</p>
<a class="abs btn hero-btn" href="#">Contact Us</a>
<div class="abs dots"><span></span><span></span><span></span><span class="on"></span></div>

<h2 class="abs sec-title" style="top:797px"><span class="mark"></span><span class="bar"></span>Services</h2>

<div class="abs service" style="left:250px;top:929px">
  <svg class="icon" viewBox="0 0 44 44"><rect x="4" y="18" width="36" height="6" fill="#222"/><circle cx="10" cy="10" r="5" fill="#222"/><circle cx="22" cy="10" r="5" fill="#222"/><circle cx="34" cy="10" r="5" fill="#222"/><rect x="8" y="26" width="4" height="14" fill="#222"/><rect x="32" y="26" width="4" height="14" fill="#222"/></svg>
  <h3>STRATEGY CONSULTING</h3>
  <p>Our team assembles our expertise that allows investors to set foot and flourish...</p>
  <span class="more">Learn More &rarr;</span>
</div>
<div class="abs service" style="left:496px;top:865px">
  <svg class="icon" viewBox="0 0 44 44"><circle cx="14" cy="14" r="7" fill="#222"/><rect x="4" y="24" width="20" height="16" rx="3" fill="#222"/><rect x="24" y="4" width="16" height="22" fill="none" stroke="#222" stroke-width="2.5"/><path d="M28 12h8M28 17h8M28 22h5" stroke="#222" stroke-width="2"/></svg>
  <h3>PROGRAMME MANAGEMENT</h3>
  <p>Our team assembles our expertise that allows investors to set foot and flourish...</p>
  <span class="more">Learn More &rarr;</span>
</div>
<div class="abs service" style="left:742px;top:929px">
  <svg class="icon" viewBox="0 0 44 44"><circle cx="22" cy="22" r="17" fill="none" stroke="#222" stroke-width="2" stroke-dasharray="20 6"/><circle cx="18" cy="20" r="6" fill="#222"/><circle cx="27" cy="26" r="5" fill="#222"/></svg>
  <h3>CHANGE MANAGEMENT</h3>
  <p>Our team assembles our expertise that allows investors to set foot and flourish...</p>
  <span class="more">Learn More &rarr;</span>
</div>

<section class="abs about" role="img" aria-label="Dark toned photo of colleagues working together at a desk"></section>
<h2 class="abs sec-title" style="top:1355px;color:#fff"><span class="mark" style="background:#fff"></span><span class="bar" style="background:#ccc"></span>About Us</h2>
<p class="abs about-text">Founded in April 2018, Marendo Consultants Limited (MCL) is an advisory consulting firm specializing in engaging investors in business ventures in Tanzania. With extensive experience in construction, energy, oil and gas and the legal professions, our team assembles our expertise that allows foreign investors to set foot and flourish in the Tanzanian market. MCL is locally owned, founded and registered. Our shareholders are cultured Tanzanian citizens with extensive corporate experience in South Africa, Kingdom and the United States.</p>
<div class="abs pillar" style="left:269px;top:1564px">
  <svg width="52" height="40" viewBox="0 0 52 40"><circle cx="26" cy="20" r="17" fill="none" stroke="var(--orange)" stroke-width="4"/><circle cx="26" cy="20" r="9" fill="none" stroke="var(--orange)" stroke-width="4"/><circle cx="26" cy="20" r="3" fill="var(--orange)"/></svg>
  <h4>Our Mission</h4>
  <p>Our mission is to provide responsive and unrivalled professional advice from learned and experienced professionals versed in the local market, with an understanding of the cultural and logistical challenges faced by foreign investors.</p>
</div>
<div class="abs pillar" style="left:632px;top:1564px">
  <svg width="60" height="40" viewBox="0 0 60 40"><path d="M4 20Q30-4 56 20Q30 44 4 20z" fill="none" stroke="var(--orange)" stroke-width="4"/><circle cx="30" cy="20" r="7" fill="var(--orange)"/></svg>
  <h4>Our Vision</h4>
  <p>Our vision is to provide a complete investor's package that initiates with company registration, compliance and documentation services and ultimately operational facilitation services.</p>
</div>

<h2 class="abs sec-title" style="top:1857px"><span class="mark"></span><span class="bar"></span>Portfolio</h2>
<div class="abs pf-text">
  <h3>PORTFOLIO 1</h3>
  <p>Founded in April 2018, Marendo Consultants Limited (MCL) is an advisory consulting firm specializing in engaging investors in Tanzania...</p>
</div>
<a class="abs btn pf-btn" href="#">Learn More &rarr;</a>
<div class="abs pf-rule"></div>
<div class="abs tile" style="left:479px;top:1927px;width:219px;height:188px" role="img" aria-label="Photo of a team gathered in a bright office"></div>
<div class="abs tile warm" style="left:706px;top:1927px;width:223px;height:336px" role="img" aria-label="Photo of a smiling businesswoman at a meeting table"></div>
<div class="abs tile warm" style="left:271px;top:2125px;width:200px;height:183px" role="img" aria-label="Photo of a business group in discussion"></div>
<div class="abs tile" style="left:271px;top:2317px;width:200px;height:141px" role="img" aria-label="Photo of colleagues reviewing documents"></div>
<div class="abs tile dark" style="left:479px;top:2125px;width:219px;height:333px" role="img" aria-label="Photo of a calculator and pen on financial charts"></div>
<div class="abs tile" style="left:706px;top:2273px;width:223px;height:185px" role="img" aria-label="Photo of hands working over charts on a desk"></div>

<footer class="abs footer"></footer>
<div class="abs f-brand"><span class="line"></span>MARENDO CONSULTANTS</div>
<p class="abs f-about">Founded in April 2018, Marendo Consultants Limited (MCL) is an advisory consulting firm specializing in engaging investors in business ventures in Tanzania. With extensive experience in construction, energy, oil and gas and the legal professions our team assembles our expertise</p>
<div class="abs f-social"><span></span><span></span><span></span><span></span></div>
<div class="abs f-contact">
  <div class="f-head" style="margin-bottom:14px">CONTACT</div>
  <p>Lorem Ipsum is dummy text<br>Printing and industry.</p>
  <p style="margin-top:12px">info@marendoconsultants.example</p>
  <p style="margin-top:12px">+1000555012</p>
  <p class="web" style="margin-top:12px">www.marendoconsultants.example</p>
</div>
<div class="abs f-links">
  <div class="f-head" style="margin-bottom:4px">QUICK LINKS</div>
  <ul><li>Home</li><li>About Us</li><li>Services</li><li>Portfolio</li><li>Contact Us</li></ul>
</div>
<div class="abs copy">&copy; Copyright 2018 Marendo Consultants. All Rights Reserved.</div>

</body>
</html>
```